professional business card

A Clean looking business card for a money transfer company. Our company is call Pavolex= Transfer + Send = Transcend (next level)
to show professionalism as well as some effects to show digital tech.

1 side to have position, name and address
2 side to have company name and show that we provide money exchange and cross-border money transfer

Target Market(s)

Remittance companies and high net worth individuals

Industry/Entity Type

Finance

Contact Information for Business Card

Name, address, email, title, services- money exchange and cross-border remittance

Requirements
Nice to have
• Digital age feel

```html
<!DOCTYPE html>
<html lang="en">
<head>
<meta charset="UTF-8">
<title>Pavolex Business Card</title>
<link href="https://fonts.googleapis.com/css2?family=Montserrat:wght@400;500;600;700&display=swap" rel="stylesheet">
<style>
  :root {
    --stage: #2b2b2b;
    --navy-deep: #061a3f;
    --navy: #0b3a80;
    --navy-teal: #0d4f6b;
    --cyan: #62d1df;
    --ink: #1d2a3a;
    --white: #ffffff;
    --coin: #f5b820;
  }
  * { margin: 0; padding: 0; box-sizing: border-box; }
  html, body {
    width: 1200px; height: 875px; overflow: hidden;
    background: var(--stage);
    font-family: "Montserrat", sans-serif;
  }
  .stage { position: relative; width: 1200px; height: 875px; }

  .card {
    position: absolute;
    width: 540px; height: 309px;
    border-radius: 18px;
    overflow: hidden;
    box-shadow: 0 18px 40px rgba(0,0,0,0.45);
  }

  /* Back side: services */
  .card-services {
    left: 50px; top: 180px;
    color: var(--white);
    background:
      radial-gradient(circle at 85% 30%, var(--navy-teal) 0%, transparent 45%),
      radial-gradient(circle at 30% 80%, var(--navy) 0%, transparent 55%),
      linear-gradient(135deg, var(--navy-deep) 0%, var(--navy) 60%, var(--navy-deep) 100%);
  }
  .brand-row {
    position: absolute; top: 44px; left: 0; right: 0;
    display: flex; justify-content: center; align-items: center; gap: 14px;
  }
  .brand-mark { width: 26px; height: 26px; background: var(--cyan); border-radius: 4px; }
  .brand-name { font-size: 46px; font-weight: 600; letter-spacing: 2px; }
  .exchange-art {
    position: absolute; left: 50%; top: 112px; transform: translateX(-50%);
    width: 104px; height: 104px; border-radius: 50%;
    background: radial-gradient(circle, var(--coin) 0%, #3c8fd8 60%, transparent 72%);
  }
  .tagline {
    position: absolute; left: 0; right: 0; bottom: 34px;
    text-align: center; font-size: 21px; font-weight: 700; line-height: 1.3;
  }

  /* Front side: contact */
  .card-contact {
    left: 610px; top: 380px;
    background: var(--white);
    color: var(--ink);
  }
  .corner-bar {
    position: absolute; top: 0; right: 0;
    width: 26px; height: 44px; background: var(--cyan);
  }
  .person { position: absolute; top: 34px; right: 44px; text-align: right; }
  .person-name { color: var(--cyan); font-size: 24px; font-weight: 700; letter-spacing: 1px; }
  .person-title { font-size: 13px; font-weight: 500; letter-spacing: 1px; margin-top: 2px; }
  .company {
    position: absolute; left: 34px; top: 112px;
    font-size: 44px; font-weight: 600; letter-spacing: 2px; color: var(--ink);
  }
  .contact-list { position: absolute; left: 36px; top: 186px; list-style: none; }
  .contact-list li {
    display: flex; align-items: center; gap: 9px;
    font-size: 14px; line-height: 22px;
  }
  .contact-list svg { width: 13px; height: 13px; fill: var(--cyan); flex: none; }
  .address {
    position: absolute; left: 36px; top: 264px;
    font-size: 14px; line-height: 20px; font-style: normal;
  }
</style>
</head>
<body>
<main class="stage">

  <section class="card card-services">
    <div class="brand-row">
      <span class="brand-mark"></span>
      <span class="brand-name">PAVOLEX</span>
    </div>
    <div class="exchange-art" role="img" aria-label="Two gold currency coins circled by blue exchange arrows"></div>
    <p class="tagline">we provide money exchange and<br>cross-border money transfer</p>
  </section>

  <section class="card card-contact">
    <div class="corner-bar"></div>
    <div class="person">
      <div class="person-name">DANIEL REYES</div>
      <div class="person-title">MANAGING DIRECTOR</div>
    </div>
    <div class="company">PAVOLEX</div>
    <ul class="contact-list">
      <li>
        <svg viewBox="0 0 24 24" aria-hidden="true"><path d="M6.6 10.8a15.2 15.2 0 0 0 6.6 6.6l2.2-2.2a1 1 0 0 1 1-.25 11.4 11.4 0 0 0 3.6.57 1 1 0 0 1 1 1V20a1 1 0 0 1-1 1A17 17 0 0 1 3 4a1 1 0 0 1 1-1h3.5a1 1 0 0 1 1 1c0 1.25.2 2.45.57 3.57a1 1 0 0 1-.25 1z"/></svg>
        044-555 210 347
      </li>
      <li>
        <svg viewBox="0 0 24 24" aria-hidden="true"><path d="M2 5h20v14H2z M2 5l10 8 10-8" /></svg>
        hello@pavolex.com
      </li>
      <li>
        <svg viewBox="0 0 24 24" aria-hidden="true"><circle cx="12" cy="12" r="10"/></svg>
        www.pavolex.com
      </li>
    </ul>
    <address class="address">87, Harbour Street<br>10234, Northland</address>
  </section>

</main>
</body>
</html>
```